Business Card Design for New Game Studio

We need a business card design. We are a new company developing innovative mobile and platform games.

I would like to see very innovative design thats brings out the company's goal and direction.

My Company's goal and direction is to "Evolve the way of gaming, Bring fun and entertainment to all gamers"

Please do use our company logo which I have attached to be included in the design.

Please put in details for name, title, contacts etc ... be creative !!!

Reason: Company logo redesign. Awaiting it. Thanks

Hi all Please do wait for my updated company logo. Thanks

Reason: Still waiting on new company logo. Thanks all

Hi All Designers .... Sorry for the long wait... Please see the new file for my new company logo uploaded. Waiting to see all your creative design. Cheers

Hi All .... Please do not just mass send a whole bunch of similar designs .... Would like to see quality instead of quantity Cheers

Entertainment

```html
<!DOCTYPE html>
<html lang="en">
<head>
<meta charset="utf-8">
<title>Novaquest Studios – Business Card</title>
<link rel="stylesheet" href="https://fonts.googleapis.com/css2?family=Open+Sans:wght@400;600;700&display=swap">
<style>
  :root {
    --page-bg: #e9e6e1;
    --card-bg: #ffffff;
    --ink: #3d3d3d;
    --ink-soft: #555555;
    --brand-green: #7dc242;
    --brand-black: #1c1c1c;
    --divider: #cfcfcf;
  }
  * { margin: 0; padding: 0; box-sizing: border-box; }
  html, body {
    width: 1200px;
    height: 720px;
    overflow: hidden;
    background: var(--page-bg);
    font-family: "Open Sans", Arial, sans-serif;
    color: var(--ink);
  }
  .canvas {
    position: relative;
    width: 1200px;
    height: 720px;
  }
  .card {
    position: absolute;
    top: 206px;
    width: 540px;
    height: 308px;
    background: var(--card-bg);
    box-shadow: 0 3px 12px rgba(0,0,0,0.12);
    overflow: hidden;
  }
  .card--front { left: 40px; }
  .card--back { left: 620px; }

  /* Front face */
  .front-brand {
    position: absolute;
    left: 28px;
    top: 104px;
    width: 240px;
    display: flex;
    align-items: center;
    gap: 12px;
  }
  .brand-dot {
    flex: none;
    width: 30px;
    height: 30px;
    border-radius: 50%;
    background: var(--brand-green);
  }
  .brand-name {
    font-weight: 700;
    font-size: 24px;
    color: var(--brand-black);
    line-height: 1.1;
  }
  .front-divider {
    position: absolute;
    left: 290px;
    top: 34px;
    width: 1px;
    height: 186px;
    background: var(--divider);
  }
  .contact {
    position: absolute;
    left: 308px;
    top: 30px;
  }
  .contact-name {
    font-weight: 700;
    font-size: 18px;
    color: var(--brand-green);
    line-height: 1.2;
  }
  .contact-title {
    font-size: 12px;
    color: var(--ink);
    margin-bottom: 8px;
  }
  .contact-list { list-style: none; }
  .contact-item {
    display: flex;
    align-items: center;
    gap: 7px;
    font-size: 12.5px;
    line-height: 19px;
    color: var(--ink);
  }
  .contact-icon { width: 13px; height: 13px; flex: none; }
  .contact-address {
    font-size: 12.5px;
    line-height: 17px;
    margin-top: 9px;
    color: var(--ink);
  }
  .front-bands {
    position: absolute;
    left: 0;
    bottom: 0;
    width: 540px;
    height: 308px;
  }

  /* Back face */
  .back-brand {
    position: absolute;
    left: 0;
    right: 0;
    top: 58px;
    display: flex;
    justify-content: center;
    align-items: center;
    gap: 14px;
  }
  .back-brand .brand-dot { width: 44px; height: 44px; }
  .back-brand .brand-name { font-size: 34px; }
  .tagline {
    position: absolute;
    left: 0;
    right: 0;
    top: 160px;
    text-align: center;
    font-size: 19px;
    line-height: 25px;
    color: var(--ink-soft);
  }
  .back-web {
    position: absolute;
    left: 0;
    right: 0;
    top: 226px;
    text-align: center;
    font-size: 18px;
    letter-spacing: 1.5px;
    color: var(--ink);
  }
</style>
</head>
<body>
<main class="canvas">

  <section class="card card--front" aria-label="Business card front">
    <div class="front-brand">
      <span class="brand-dot" aria-hidden="true"></span>
      <span class="brand-name">Novaquest Studios</span>
    </div>

    <div class="front-divider" aria-hidden="true"></div>

    <div class="contact">
      <p class="contact-name">Your Name</p>
      <p class="contact-title">Title</p>
      <ul class="contact-list">
        <li class="contact-item">
          <svg class="contact-icon" viewBox="0 0 14 14" aria-hidden="true"><circle cx="7" cy="7" r="6.5" fill="var(--brand-green)"/><path d="M4.5 3.5l1.5 0 .6 2-1 .8a5 5 0 0 0 2.1 2.1l.8-1 2 .6v1.5a1 1 0 0 1-1 1A6 6 0 0 1 3.5 4.5a1 1 0 0 1 1-1z" fill="#fff"/></svg>
          012-345-6789
        </li>
        <li class="contact-item">
          <svg class="contact-icon" viewBox="0 0 14 14" aria-hidden="true"><circle cx="7" cy="7" r="6.5" fill="var(--brand-green)"/><rect x="4.8" y="3" width="4.4" height="8" rx="0.8" fill="#fff"/><rect x="5.5" y="4" width="3" height="4.6" fill="var(--brand-green)"/></svg>
          012-345-6789
        </li>
        <li class="contact-item">
          <svg class="contact-icon" viewBox="0 0 14 14" aria-hidden="true"><circle cx="7" cy="7" r="6.5" fill="var(--brand-green)"/><rect x="3.5" y="4.5" width="7" height="5" fill="#fff"/><path d="M3.5 4.5L7 7.5l3.5-3" stroke="var(--brand-green)" stroke-width="0.9" fill="none"/></svg>
          info@novaquestplay.com
        </li>
        <li class="contact-item">
          <svg class="contact-icon" viewBox="0 0 14 14" aria-hidden="true"><circle cx="7" cy="7" r="6.5" fill="var(--brand-green)"/><circle cx="7" cy="7" r="3.6" fill="none" stroke="#fff" stroke-width="1"/><path d="M3.4 7h7.2M7 3.4c-1.6 2-1.6 5.2 0 7.2M7 3.4c1.6 2 1.6 5.2 0 7.2" stroke="#fff" stroke-width="0.8" fill="none"/></svg>
          www.novaquestplay.com
        </li>
      </ul>
      <p class="contact-address">Street Name, City Name<br>Zip Code - 000000</p>
    </div>

    <svg class="front-bands" viewBox="0 0 540 308" aria-hidden="true">
      <polygon points="316,260 540,260 540,282 296,282" fill="var(--brand-black)"/>
      <polygon points="0,286 294,286 284,296 0,296" fill="var(--brand-green)"/>
    </svg>
  </section>

  <section class="card card--back" aria-label="Business card back">
    <div class="back-brand">
      <span class="brand-dot" aria-hidden="true"></span>
      <span class="brand-name">Novaquest Studios</span>
    </div>
    <p class="tagline">Evolve The Way Of Gaming, Bring Fun And<br>Entertainment To All Gamers</p>
    <p class="back-web">www.novaquestplay.com</p>
  </section>

</main>
</body>
</html>
```